Engaging online lending company website

We already have a website at www.corvelfunding.com.au however it's nowhere near engaging enough. We are a fintech online brokerage company providing fantastic and super quick turnaround times on vehicle and mortgage loans. We need a website that is engaging with lots of call to actions and quote forms to capture details.

Target Market(s)

Young, technology savvy Australian's requiring finance. Aged between 20 - 45

Industry/Entity Type

Finance

Coding

Coded - Design and coding required

Requirements
Must have
• Get a Quick Quote Call to Action Box
• Get a Quick Quote (Express)
• Calculator Designs (2) – Home loan repayment and car loan repayment
• How it Works – Engaging design showing our 4 step loans process
• Banners: 1x for lending panel, 1 for current interest rates (similar to marlow capital home page), 1x Quill Nest for customer reviews
• Banner on each page: Similar to Orbi Finance “Today’s Best Rate” see below:
• Lots of well placed call to action buttons and quick quote forms on each page
• Apply Now page (similar fields to: https://www.marlowcapitalgroup.com.au/pre-approval/)

```html
<!DOCTYPE html>
<html lang="en">
<head>
<meta charset="utf-8">
<title>Brightway Lending Solutions</title>
<link rel="stylesheet" href="https://fonts.googleapis.com/css2?family=Open+Sans:wght@400;600;700;800&display=swap">
<style>
:root{
  --navy:#16405e;
  --navy-deep:#0e3652;
  --navy-bottom:#0b2f48;
  --blue:#1ba2d2;
  --blue-card:#1ea5d4;
  --blue-dark:#14577d;
  --orange:#fb7f16;
  --yellow:#fdb813;
  --grey-band:#ececec;
  --grey-step:#f0f0f0;
  --grey-line:#d9d9d9;
  --text:#2e3d4a;
  --muted:#6b7580;
  --white:#ffffff;
  --star:#f79a1b;
}
*{box-sizing:border-box;margin:0;padding:0}
html,body{width:1200px;height:3000px;overflow:hidden;background:var(--white)}
body{font-family:"Open Sans",Arial,sans-serif;color:var(--text);position:relative}
.abs{position:absolute}

/* header */
.brand{left:76px;top:32px}
.brand-name{font-size:40px;font-weight:800;color:var(--blue-dark);letter-spacing:1px;line-height:1}
.brand-tag{font-size:14px;font-weight:600;color:var(--blue);letter-spacing:4px;margin-top:4px}
.service{right:76px;top:26px;display:flex;align-items:center;gap:18px}
.service-text{text-align:right}
.service-label{font-size:13px;font-weight:700;color:var(--blue)}
.service-phone{font-size:31px;font-weight:700;color:var(--blue);line-height:1.1}

/* nav */
.main-nav{left:76px;top:108px;width:1048px;height:52px;background:var(--navy);display:flex;align-items:center;padding-left:20px;z-index:3}
.nav-item{display:flex;align-items:center;gap:10px;color:var(--white);font-size:13px;font-weight:700;margin-right:46px}
.nav-btn{position:absolute;right:6px;top:6px;height:40px;width:158px;background:var(--blue);color:var(--white);font-size:13px;font-weight:700;display:flex;align-items:center;justify-content:center}

/* hero */
.hero{left:0;top:132px;width:1200px;height:538px;background:linear-gradient(#8fd3ee 0%,#c9ecf8 45%,#9ccf4a 60%,#8a8f95 75%,#c4c7cb 100%)}
.quote-box{left:702px;top:222px;width:424px;height:402px;background:var(--white);box-shadow:0 2px 10px rgba(0,0,0,.2);padding:22px 22px 0;text-align:center}
.quote-title{font-size:27px;font-weight:700;color:var(--navy-deep);letter-spacing:.5px}
.quote-sub{font-size:12px;color:var(--muted);margin-top:4px}
.loan-icons{display:flex;justify-content:center;gap:44px;margin:14px 0 12px}
.field-row{display:flex;gap:8px;margin-bottom:10px;padding:0 0 0 0}
.field{flex:1;height:36px;border:1px solid #c9c9c9;font-size:12px;color:#8a8f95;text-align:left;padding:10px 10px}
.purpose{display:flex;align-items:center;font-size:12px;color:var(--navy-deep);font-weight:600;margin:14px 0 14px}
.radio{width:12px;height:12px;border:1px solid #999;border-radius:50%;display:inline-block;margin:0 8px 0 24px;vertical-align:-1px}
.quote-btn{height:44px;background:var(--yellow);color:var(--white);font-size:16px;font-weight:700;display:flex;align-items:center;justify-content:center;letter-spacing:.5px}
.quote-terms{font-size:11px;color:var(--text);margin-top:10px;line-height:1.5}

/* rates */
.rates{left:0;top:670px;width:1200px;height:220px;background:linear-gradient(#ffffff,#ededed)}
.rate-label{left:76px;top:732px;width:352px;height:46px;background:var(--orange);color:var(--white);font-size:21px;display:flex;align-items:center;justify-content:center}
.rate-date{left:76px;top:778px;width:352px;height:56px;background:#eaeaea;font-size:20px;font-weight:600;display:flex;align-items:center;justify-content:center;gap:12px;color:var(--text)}
.rate-box{top:730px;height:106px;background:var(--white);border:1px solid #cfd6dc;padding:10px 20px}
.rate-kicker{font-size:18px;color:var(--blue)}
.rate-value{font-size:54px;color:var(--navy-deep);line-height:1;margin-top:2px}
.rate-value sup{font-size:26px;vertical-align:22px;margin-left:6px}
.rate-note{position:absolute;right:14px;bottom:12px;font-size:14px;color:var(--navy-deep)}

/* how it works */
.section-title{width:1200px;left:0;text-align:center;font-size:27px;font-weight:700;color:var(--navy-deep);letter-spacing:.5px}
.step{top:1020px;width:204px;height:204px;background:var(--grey-step);border:1px solid #e3e3e3;text-align:center}
.step-icon{width:78px;height:78px;border:2px solid #c9cdd1;border-radius:50%;margin:28px auto 0;position:relative;background:var(--white);display:flex;align-items:center;justify-content:center}
.step-num{position:absolute;left:-10px;top:-8px;width:32px;height:32px;border-radius:50%;background:var(--blue);color:var(--white);font-size:15px;font-weight:700;display:flex;align-items:center;justify-content:center}
.step-name{font-size:17px;font-weight:700;color:var(--blue);margin-top:14px}
.step-desc{font-size:12px;color:var(--text);margin-top:4px;line-height:1.6;text-transform:uppercase;padding:0 20px}
.step-arrow{top:1108px}

/* partners */
.partners{left:0;top:1280px;width:1200px;height:204px;background:var(--grey-band)}
.partner{top:1362px;font-size:30px;font-weight:700;color:#2d2d2d;text-align:center;width:220px}

/* loan cards */
.loan-card{top:1620px;width:246px;height:260px;background:var(--blue-card);text-align:center;color:var(--white);padding-top:72px}
.loan-ring{top:1534px;width:140px;height:140px;border-radius:50%;background:var(--blue-card);display:flex;align-items:center;justify-content:center}
.loan-ring-inner{width:118px;height:118px;border-radius:50%;background:linear-gradient(#ffffff,#dbeff7)}
.loan-name{font-size:19px}
.loan-rate{font-size:38px;font-weight:700;margin-top:4px}
.loan-comp{font-size:10px;margin-top:8px}
.apply-btn{display:inline-block;margin-top:18px;width:110px;height:42px;line-height:42px;background:var(--navy);font-size:14px;font-weight:600;border-radius:3px;box-shadow:0 2px 0 rgba(0,0,0,.25)}

/* reviews */
.review{top:2014px;width:286px;height:162px;border:1px solid var(--grey-line);background:var(--white);padding:22px 20px}
.review-top{display:flex;justify-content:space-between;align-items:center;font-size:11px;color:var(--muted)}
.stars{color:var(--star);font-size:16px;letter-spacing:2px}
.review-text{font-size:14px;line-height:1.55;margin-top:12px;color:var(--text)}
.reviewer{display:flex;align-items:center;justify-content:space-between;font-size:13px;font-weight:600;color:var(--blue);margin-top:2px}
.avatar{width:38px;height:38px;border-radius:50%;background:linear-gradient(#e9c9a8,#c79a73)}
.rated{left:0;top:2204px;width:1200px;text-align:center;font-size:10px;color:var(--muted);line-height:1.8}

/* promo */
.promo{left:0;top:2268px;width:1200px;height:416px;background:var(--blue)}
.mascot{left:76px;top:2290px;width:220px;height:394px;background:linear-gradient(#f2d2b4 0%,#f2d2b4 30%,#ffffff 31%,#ffffff 62%,#1f6f9a 63%,#1f6f9a 100%);border-radius:90px 90px 10px 10px}
.promo-title{left:400px;top:2344px;font-size:31px;font-weight:600;color:var(--white)}
.promo-text{left:400px;top:2404px;width:790px;font-size:19px;line-height:1.6;color:var(--white)}
.outline-btn{top:2496px;height:58px;border:2px solid rgba(255,255,255,.75);color:var(--white);font-size:21px;display:flex;align-items:center;justify-content:center;letter-spacing:.5px}

/* footer */
.footer{left:0;top:2684px;width:1200px;height:240px;background:var(--navy)}
.foot-brand{left:76px;top:2730px;color:var(--white)}
.foot-brand .brand-name{color:var(--white);font-size:30px}
.foot-brand .brand-tag{color:var(--white);font-size:12px;letter-spacing:3px}
.foot-about{left:76px;top:2806px;width:240px;font-size:14px;line-height:1.6;color:var(--white)}
.foot-col{top:2728px;color:var(--white)}
.foot-head{font-size:14px;font-weight:700;color:var(--blue);margin-bottom:14px;letter-spacing:.5px}
.foot-link{font-size:14px;line-height:32px}
.bottom-bar{left:0;top:2924px;width:1200px;height:76px;background:var(--navy-bottom);color:var(--white);font-size:12px;padding:34px 76px 0}
.socials{right:76px;top:2948px;display:flex;gap:18px}
.social-dot{width:22px;height:22px;border-radius:50%;background:var(--white)}
</style>
</head>
<body>

<!-- header -->
<div class="abs brand">
  <div class="brand-name">BRIGHTWAY</div>
  <div class="brand-tag">LENDING SOLUTIONS</div>
</div>
<div class="abs service">
  <svg width="40" height="40" viewBox="0 0 40 40"><circle cx="20" cy="20" r="18" fill="none" stroke="#1ba2d2" stroke-width="2.5"/><path d="M14 11c2 0 3 4 2 5l-2 2c1 3 4 6 7 7l2-2c1-1 5 0 5 2l-1 3c-8 1-16-7-15-15z" fill="#1ba2d2"/></svg>
  <div class="service-text">
    <div class="service-label">24/7 Custmer Service</div>
    <div class="service-phone">1300 482 619</div>
  </div>
</div>

<!-- hero -->
<div class="abs hero" role="img" aria-label="Illustration of a smiling family driving a blue car along a winding road through green hills under a blue sky"></div>

<nav class="abs main-nav">
  <div class="nav-item"><svg width="16" height="12" viewBox="0 0 16 12"><rect x="1" y="4" width="14" height="6" rx="2" fill="#1ba2d2"/><rect x="4" y="1" width="8" height="4" rx="1" fill="#1ba2d2"/></svg>CAR LOANS</div>
  <div class="nav-item"><svg width="14" height="14" viewBox="0 0 14 14"><path d="M7 1L1 7h2v6h8V7h2z" fill="#1ba2d2"/></svg>HOME LOANS</div>
  <div class="nav-item"><svg width="14" height="13" viewBox="0 0 14 13"><rect x="1" y="3" width="12" height="9" rx="1" fill="#1ba2d2"/><rect x="5" y="1" width="4" height="3" fill="none" stroke="#1ba2d2"/></svg>COMMERCIAL LOANS</div>
  <div class="nav-item"><svg width="12" height="14" viewBox="0 0 12 14"><circle cx="6" cy="4" r="3" fill="#1ba2d2"/><path d="M1 13c0-4 10-4 10 0z" fill="#1ba2d2"/></svg>PERSONAL LOANS</div>
  <div class="nav-btn">GET PRE APPROVED</div>
</nav>

<section class="abs quote-box">
  <div class="quote-title">GET A QUICK QUOTE</div>
  <div class="quote-sub">Select a loan type from the icons below</div>
  <div class="loan-icons">
    <svg width="22" height="16" viewBox="0 0 22 16"><rect x="1" y="6" width="20" height="7" rx="2" fill="#1ba2d2"/><rect x="5" y="2" width="12" height="5" rx="1" fill="#1ba2d2"/></svg>
    <svg width="20" height="18" viewBox="0 0 20 18"><rect x="1" y="5" width="18" height="12" rx="1" fill="#1ba2d2"/><rect x="7" y="1" width="6" height="5" fill="none" stroke="#1ba2d2" stroke-width="2"/></svg>
    <svg width="20" height="18" viewBox="0 0 20 18"><path d="M10 1L1 9h3v8h12V9h3z" fill="#1ba2d2"/></svg>
    <svg width="16" height="18" viewBox="0 0 16 18"><circle cx="8" cy="5" r="4" fill="#1ba2d2"/><path d="M1 17c0-6 14-6 14 0z" fill="#1ba2d2"/></svg>
  </div>
  <div class="field-row"><div class="field">First Name</div><div class="field">Last Name</div></div>
  <div class="field-row"><div class="field">Email Address</div></div>
  <div class="field-row"><div class="field">Phone No</div><div class="field">Postal Code</div></div>
  <div class="purpose">Finance For Business Purposes <span class="radio"></span>No <span class="radio" style="margin-left:16px"></span>Yes</div>
  <div class="quote-btn">GET MY QUOTE</div>
  <div class="quote-terms">By clicking Get My Quote,<br>I acknowledge and accept the Terms &amp; Conditions.</div>
</section>

<!-- rates -->
<div class="abs rates"></div>
<div class="abs rate-label">TODAY'S BEST RATE ON</div>
<div class="abs rate-date">
  <svg width="20" height="20" viewBox="0 0 20 20"><rect x="2" y="4" width="16" height="14" fill="none" stroke="#6b7580" stroke-width="2"/><line x1="2" y1="8" x2="18" y2="8" stroke="#6b7580" stroke-width="2"/><line x1="6" y1="1" x2="6" y2="5" stroke="#6b7580" stroke-width="2"/><line x1="14" y1="1" x2="14" y2="5" stroke="#6b7580" stroke-width="2"/></svg>
  MON, MAR 06 2017
</div>
<div class="abs rate-box" style="left:472px;width:306px">
  <div class="rate-kicker">HOME LOANS FROM</div>
  <div class="rate-value">3.94<sup>%</sup></div>
  <div class="rate-note">FIXED</div>
</div>
<div class="abs rate-box" style="left:820px;width:304px">
  <div class="rate-kicker">WITH A LOW</div>
  <div class="rate-value">2.54<sup>%</sup></div>
  <div class="rate-note">COMPARISION</div>
</div>

<!-- how it works -->
<h2 class="abs section-title" style="top:940px">HOW IT WORKS</h2>

<div class="abs step" style="left:76px">
  <div class="step-icon"><span class="step-num">1</span><svg width="34" height="30" viewBox="0 0 34 30"><rect x="3" y="4" width="28" height="18" rx="2" fill="none" stroke="#2e3d4a" stroke-width="2"/><line x1="12" y1="27" x2="22" y2="27" stroke="#2e3d4a" stroke-width="2"/></svg></div>
  <div class="step-name">APPLY</div><div class="step-desc">Online now</div>
</div>
<div class="abs step" style="left:358px">
  <div class="step-icon"><span class="step-num">2</span><svg width="30" height="32" viewBox="0 0 30 32"><rect x="5" y="3" width="20" height="26" rx="2" fill="none" stroke="#2e3d4a" stroke-width="2"/><path d="M10 16l4 4 7-8" fill="none" stroke="#2e3d4a" stroke-width="2"/></svg></div>
  <div class="step-name">APPROVED</div><div class="step-desc">Instantly</div>
</div>
<div class="abs step" style="left:644px">
  <div class="step-icon"><span class="step-num">3</span><svg width="34" height="30" viewBox="0 0 34 30"><circle cx="13" cy="13" r="9" fill="none" stroke="#2e3d4a" stroke-width="2"/><circle cx="22" cy="18" r="9" fill="#fff" stroke="#2e3d4a" stroke-width="2"/><text x="22" y="22" font-size="11" text-anchor="middle" fill="#2e3d4a" font-family="Open Sans,sans-serif">$</text></svg></div>
  <div class="step-name">FUNDED</div><div class="step-desc">Today or deposited overnight</div>
</div>
<div class="abs step" style="left:928px">
  <div class="step-icon"><span class="step-num">4</span><svg width="32" height="32" viewBox="0 0 32 32"><rect x="6" y="3" width="20" height="26" rx="3" fill="none" stroke="#2e3d4a" stroke-width="2"/><path d="M10 12h12l-3-3M22 20H10l3 3" fill="none" stroke="#2e3d4a" stroke-width="2"/></svg></div>
  <div class="step-name">REPAY</div><div class="step-desc">On your next pay period</div>
</div>

<svg class="abs step-arrow" style="left:290px" width="60" height="26" viewBox="0 0 60 26"><line x1="0" y1="13" x2="40" y2="13" stroke="#1ba2d2" stroke-width="4" stroke-dasharray="4 5"/><path d="M40 2l18 11-18 11z" fill="#1ba2d2"/></svg>
<svg class="abs step-arrow" style="left:574px" width="60" height="26" viewBox="0 0 60 26"><line x1="0" y1="13" x2="40" y2="13" stroke="#1ba2d2" stroke-width="4" stroke-dasharray="4 5"/><path d="M40 2l18 11-18 11z" fill="#1ba2d2"/></svg>
<svg class="abs step-arrow" style="left:858px" width="60" height="26" viewBox="0 0 60 26"><line x1="0" y1="13" x2="40" y2="13" stroke="#1ba2d2" stroke-width="4" stroke-dasharray="4 5"/><path d="M40 2l18 11-18 11z" fill="#1ba2d2"/></svg>

<!-- lending panel -->
<div class="abs partners"></div>
<svg class="abs" style="left:74px;top:1368px" width="16" height="28" viewBox="0 0 16 28"><path d="M14 2L3 14l11 12" fill="none" stroke="#9a9a9a" stroke-width="3"/></svg>
<svg class="abs" style="left:1108px;top:1368px" width="16" height="28" viewBox="0 0 16 28"><path d="M2 2l11 12L2 26" fill="none" stroke="#9a9a9a" stroke-width="3"/></svg>
<div class="abs partner" style="left:98px">Fundora</div>
<div class="abs partner" style="left:360px">Kestrel</div>
<div class="abs partner" style="left:614px;font-size:24px">Harbour Capital</div>
<div class="abs partner" style="left:876px">Northbank</div>

<!-- loan products -->
<div class="abs loan-ring" style="left:129px"><div class="loan-ring-inner" role="img" aria-label="Illustration of a salesman beside a car"></div></div>
<div class="abs loan-ring" style="left:395px"><div class="loan-ring-inner" role="img" aria-label="Illustration of an agent beside a house"></div></div>
<div class="abs loan-ring" style="left:663px"><div class="loan-ring-inner" role="img" aria-label="Illustration of a rider with a motorbike"></div></div>
<div class="abs loan-ring" style="left:931px"><div class="loan-ring-inner" role="img" aria-label="Illustration of a driver beside a delivery van"></div></div>

<div class="abs loan-card" style="left:76px"><div class="loan-name">Car Loans – From</div><div class="loan-rate">4.20 %</div><div class="loan-comp">5.07% COMPARISON RATE</div><div class="apply-btn">Apply Now</div></div>
<div class="abs loan-card" style="left:342px"><div class="loan-name">Home Loans – From</div><div class="loan-rate">3.89 %</div><div class="loan-comp">3.99% COMPARISON RATE</div><div class="apply-btn">Apply Now</div></div>
<div class="abs loan-card" style="left:610px"><div class="loan-name">Bike Loans – From</div><div class="loan-rate">6.69 %</div><div class="loan-comp">7.49% COMPARISON RATE</div><div class="apply-btn">Apply Now</div></div>
<div class="abs loan-card" style="left:878px"><div class="loan-name">Business Loans – From</div><div class="loan-rate">4.20 %</div><div class="loan-comp">4.99% COMPARISON RATE</div><div class="apply-btn">Apply Now</div></div>

<!-- reviews -->
<h2 class="abs section-title" style="top:1932px">CUSTOMER REVIEWS</h2>
<svg class="abs" style="left:76px;top:2082px" width="14" height="24" viewBox="0 0 14 24"><path d="M12 2L3 12l9 10" fill="none" stroke="#9a9a9a" stroke-width="3"/></svg>
<svg class="abs" style="left:1108px;top:2082px" width="14" height="24" viewBox="0 0 14 24"><path d="M2 2l9 10-9 10" fill="none" stroke="#9a9a9a" stroke-width="3"/></svg>

<div class="abs review" style="left:142px">
  <div class="review-top"><span class="stars">★★★★★</span><span>6 days ago</span></div>
  <div class="review-text">Vestibulum ante ipsum primis in faucibus orci luctus et ultrices posuere cubilia</div>
  <div class="reviewer">Mara Ellison<span class="avatar" role="img" aria-label="Reviewer portrait"></span></div>
</div>
<div class="abs review" style="left:458px">
  <div class="review-top"><span class="stars">★★★★★</span><span>6 days ago</span></div>
  <div class="review-text">Vestibulum ante ipsum primis in faucibus orci luctus et ultrices posuere cubilia</div>
  <div class="reviewer">Mara Ellison<span class="avatar" role="img" aria-label="Reviewer portrait"></span></div>
</div>
<div class="abs review" style="left:772px">
  <div class="review-top"><span class="stars">★★★★★</span><span>6 days ago</span></div>
  <div class="review-text">Vestibulum ante ipsum primis in faucibus orci luctus et ultrices posuere cubilia</div>
  <div class="reviewer">Mara Ellison<span class="avatar" role="img" aria-label="Reviewer portrait"></span></div>
</div>
<div class="abs rated">Rated <b>9.3</b> out of 10 based on <b>495</b> reviews. See some of the reviews here.<br>Powered by <b>QUILL NEST</b></div>

<!-- promo -->
<div class="abs promo"></div>
<div class="abs mascot" role="img" aria-label="Cartoon mascot in a white branded shirt and jeans standing with hands on hips"></div>
<div class="abs promo-title">Finance at your fingertips</div>
<div class="abs promo-text">Make a request on our website and wait for response to e-mail within 15-30 minutes from the time of the request during business hours.</div>
<div class="abs outline-btn" style="left:400px;width:300px">HOME LOAN REPAYMENT</div>
<div class="abs outline-btn" style="left:734px;width:300px">CAR LOAN REPAYMENT</div>

<!-- footer -->
<footer>
  <div class="abs footer"></div>
  <div class="abs foot-brand"><div class="brand-name">BRIGHTWAY</div><div class="brand-tag">LENDING SOLUTIONS</div></div>
  <div class="abs foot-about">Brightway Lending Solutions is a trading name of Hollin Auto Finance Pty Ltd</div>
  <div class="abs foot-col" style="left:386px">
    <div class="foot-head">SITE MAP</div>
    <div class="foot-link">Car Loans</div><div class="foot-link">Personal Loans</div><div class="foot-link">Home Loans</div><div class="foot-link">Commercial Loans</div>
  </div>
  <div class="abs foot-col" style="left:604px">
    <div class="foot-head">EXTRA LINKS</div>
    <div class="foot-link">Privacy</div><div class="foot-link">Terms &amp; Conditions</div><div class="foot-link">Credit Guide &amp; Quote</div><div class="foot-link">Investor relations</div>
  </div>
  <div class="abs foot-col" style="left:848px">
    <div class="foot-head">OPEN HOURS</div>
    <div class="foot-link">Monday 8am-7pm</div><div class="foot-link">Tuesday-Friday 8am-6pm</div><div class="foot-link">Saturday 10am-2pm</div><div class="foot-link">Sunday CLOSED</div>
  </div>
  <div class="abs bottom-bar">Copyright © 2017. Company Name. All Right Reserved</div>
  <div class="abs socials"><span class="social-dot"></span><span class="social-dot"></span><span class="social-dot"></span><span class="social-dot"></span><span class="social-dot"></span><span class="social-dot"></span></div>
</footer>

</body>
</html>
```